Packaging Label Graphic Design

This design is for new packaging that we are about to launch. This label will go around our food container. We are hoping to go with some parts of the label clear (so you can still see the food inside) and the other half colored. We are open to your creativity. I will attached our logo , as that will need to be on there. As well as our website www.brindlepantry.com, as well as instagram @brindlepantry. We use the slogan "Elevate Your Life". You can use that too.
Our food is a healthier concept, and our food has a high volume of fresh ingredients. These containers will particularly be used for our Meal Prep(Fully cooked meals that you just need to heat up). The final design should look so goo that you would want to put it on your instagram before eating it :) The colours we currently play around with are navy blue, the grey and green you see in our logo, we also have a mustard colour that we have been implementing. Sizes that it needs to be is attached.

Target Market(s)

Ages 25-35

Requirements
Must have
• Our logo, website, & social media handles, a clear patch (with a design in it) so customers can see the food better. Get Creative.
Nice to have
• Color , stand out to customers, distinguished look.

```html
<!DOCTYPE html>
<html lang="en">
<head>
<meta charset="utf-8">
<title>Brindle Meal Prep Sleeve Label</title>
<link href="https://fonts.googleapis.com/css2?family=Montserrat:wght@500;700;800&family=Great+Vibes&display=swap" rel="stylesheet">
<style>
  :root {
    --canvas-bg: #ececec;
    --brand-green: #93c01f;
    --film-dark: #3b3738;
    --text-white: #ffffff;
    --food-rice: #a08a6e;
    --food-greens: #4d6a34;
    --food-chicken: #b58a5e;
    --food-carrot: #b0572a;
  }
  html, body {
    margin: 0;
    padding: 0;
    width: 1200px;
    height: 1080px;
    overflow: hidden;
    background: var(--canvas-bg);
    font-family: "Montserrat", sans-serif;
  }
  .canvas {
    position: relative;
    width: 1200px;
    height: 1080px;
  }
  .sleeve {
    position: absolute;
    left: 397px;
    top: 60px;
    width: 405px;
    height: 960px;
    background: var(--film-dark);
    box-shadow: 0 18px 40px rgba(0,0,0,0.18);
    overflow: hidden;
  }
  .sleeve-header {
    position: absolute;
    left: 0;
    top: 0;
    width: 405px;
    height: 136px;
    background: var(--brand-green);
  }
  .clear-window {
    position: absolute;
    left: 0;
    top: 136px;
    width: 405px;
    height: 688px;
    background:
      radial-gradient(circle at 20% 12%, var(--food-rice) 0 18%, transparent 34%),
      radial-gradient(circle at 15% 88%, var(--food-carrot) 0 10%, transparent 26%),
      radial-gradient(circle at 40% 60%, var(--food-greens) 0 20%, transparent 42%),
      radial-gradient(circle at 90% 50%, var(--food-chicken) 0 18%, transparent 40%),
      linear-gradient(160deg, #8a745c 0%, #5a6a3e 50%, #8c6a4c 100%);
  }
  .window-tint {
    position: absolute;
    left: 0;
    top: 136px;
    width: 405px;
    height: 688px;
    background: rgba(40, 36, 37, 0.38);
  }
  .mark-placeholder {
    position: absolute;
    left: 128px;
    top: 64px;
    width: 260px;
    height: 260px;
    border-radius: 50%;
    background: var(--text-white);
  }
  .vertical {
    position: absolute;
    writing-mode: vertical-rl;
    transform: rotate(180deg);
    white-space: nowrap;
  }
  .slogan {
    left: 36px;
    bottom: 255px;
    font-family: "Great Vibes", cursive;
    line-height: 1;
  }
  .slogan-lead {
    color: var(--brand-green);
    font-size: 30px;
  }
  .slogan-life {
    color: var(--text-white);
    font-size: 72px;
  }
  .brand-name {
    left: 170px;
    bottom: 160px;
    font-size: 70px;
    font-weight: 800;
    letter-spacing: 2px;
    color: var(--text-white);
    line-height: 1;
  }
  .brand-dot {
    position: absolute;
    left: 188px;
    bottom: 122px;
    width: 26px;
    height: 26px;
    border-radius: 50%;
    background: var(--brand-green);
  }
  .tagline {
    left: 244px;
    bottom: 160px;
    font-size: 24px;
    font-weight: 700;
    color: var(--brand-green);
    line-height: 1;
  }
  .contacts {
    left: 296px;
    bottom: 270px;
    display: flex;
    gap: 8px;
  }
  .contact-line {
    display: flex;
    align-items: center;
    gap: 8px;
    font-size: 15px;
    font-weight: 500;
    color: var(--text-white);
  }
  .contact-icon {
    width: 16px;
    height: 16px;
    border-radius: 50%;
    background: var(--brand-green);
  }
</style>
</head>
<body>
  <main class="canvas">
    <section class="sleeve">
      <div class="clear-window" role="img" aria-label="Clear window showing the meal inside: grilled chicken, shrimp, brown rice, greens and carrots"></div>
      <div class="window-tint"></div>
      <div class="sleeve-header"></div>
      <div class="mark-placeholder"></div>

      <div class="vertical slogan">
        <span class="slogan-lead">Elevate Your</span>
        <span class="slogan-life">Life</span>
      </div>

      <div class="vertical brand-name">BRINDLE</div>
      <div class="brand-dot"></div>

      <div class="vertical tagline">HEALTHY KITCHEN | MEAL PREP</div>

      <div class="vertical contacts">
        <div class="contact-line"><span class="contact-icon"></span>@brindlepantry</div>
        <div class="contact-line"><span class="contact-icon"></span>www.brindlepantry.com</div>
      </div>
    </section>
  </main>
</body>
</html>
```